Crimson Lantern Harbor, Topics; Nursing, Military, Family and Faith

Three word Title with topics underlined beneath.
It will be a book cover on which I would like to capture a Vision of each topic if possible.

It is a 9"x 6" single book blending the 4 topics throughout the text.
I had a the title and topics framed in the middle, with pics of nature above and below but would like something different that catches the eye relating more to the text.

Target Market(s)

Nurses, patients and family, Non-Christians / Christians, and Military.

Font styles to use
Script

Colors

Requirements
Must have
• Title underlined by topics, over illustrated background
Nice to have
• If possible, use topics for background behind the title.

```html
<!DOCTYPE html>
<html lang="en">
<head>
<meta charset="utf-8">
<title>Crimson Lantern Harbor – Cover Series</title>
<link href="https://fonts.googleapis.com/css2?family=Great+Vibes&family=Cormorant+Garamond:wght@500&display=swap" rel="stylesheet">
<style>
  :root {
    --page-bg: #ffffff;
    --ink-light: #ffffff;
    --rule: rgba(255,255,255,0.8);
    --nursing: #4a1a63;
    --family: #172a60;
    --military: #1e6a12;
  }
  html, body {
    margin: 0;
    width: 1200px;
    height: 1000px;
    overflow: hidden;
    background: var(--page-bg);
  }
  .series {
    position: relative;
    width: 1200px;
    height: 1000px;
  }
  .cover {
    position: absolute;
    top: 232px;
    width: 377px;
    height: 548px;
    overflow: hidden;
    background: var(--tone);
    box-shadow: 3px 4px 6px rgba(0,0,0,0.35);
  }
  .cover--nursing { left: 18px; --tone: var(--nursing); }
  .cover--family { left: 415px; --tone: var(--family); }
  .cover--military { left: 812px; --tone: var(--military); }

  .cover-photo {
    position: absolute;
    left: 0; top: 0;
    width: 100%;
    height: 320px;
  }
  .cover--nursing .cover-photo {
    background:
      linear-gradient(to bottom, rgba(74,26,99,0) 30%, rgba(74,26,99,0.7) 70%, var(--nursing) 96%),
      radial-gradient(ellipse 90px 120px at 70px 130px, #b9aec8 0%, rgba(185,174,200,0) 100%),
      radial-gradient(ellipse 100px 130px at 230px 140px, #a99bb8 0%, rgba(169,155,184,0) 100%),
      linear-gradient(90deg, #7a6a86 0%, #e2dbe6 30%, #d3cad9 70%, #3a4a6a 100%);
  }
  .cover--family .cover-photo {
    background:
      linear-gradient(to bottom, rgba(23,42,96,0) 40%, rgba(23,42,96,0.6) 75%, var(--family) 96%),
      radial-gradient(ellipse 170px 110px at 190px 190px, #c9b79e 0%, rgba(201,183,158,0) 100%),
      linear-gradient(180deg, #e6df9c 0%, #b9ae86 45%, #7d7a6e 100%);
  }
  .cover--military .cover-photo {
    background:
      linear-gradient(to bottom, rgba(30,106,18,0) 35%, rgba(30,106,18,0.7) 70%, var(--military) 96%),
      radial-gradient(ellipse 110px 170px at 210px 170px, #8a8f70 0%, rgba(138,143,112,0) 100%),
      linear-gradient(90deg, #b8b8a4 0%, #d8d6c8 40%, #cfcfc0 80%, #e1e1d6 100%);
  }
  .title-ring {
    position: absolute;
    left: 62px; top: 146px;
    width: 254px; height: 254px;
    border: 1px solid var(--rule);
    border-radius: 50%;
    box-sizing: border-box;
  }
  .title-block {
    position: absolute;
    left: 0; top: 208px;
    width: 100%;
    text-align: center;
    color: var(--ink-light);
  }
  .book-title {
    margin: 0;
    font-family: "Great Vibes", cursive;
    font-weight: 400;
    font-size: 36px;
    line-height: 34px;
    text-shadow: 0 1px 3px rgba(0,0,0,0.3);
  }
  .topic {
    width: 225px;
    margin: 13px auto 0;
    padding: 1px 0 2px;
    border-top: 1px solid var(--rule);
    border-bottom: 1px solid var(--rule);
    font-family: "Cormorant Garamond", serif;
    font-weight: 500;
    font-size: 25px;
    line-height: 27px;
    letter-spacing: 2.5px;
    text-transform: uppercase;
  }
  .topic--long { font-size: 20px; letter-spacing: 1.5px; }
  .author {
    position: absolute;
    left: 0; top: 496px;
    width: 100%;
    text-align: center;
    font-family: "Cormorant Garamond", serif;
    font-weight: 500;
    font-size: 25px;
    color: var(--ink-light);
  }
</style>
</head>
<body>
<main class="series">
  <article class="cover cover--nursing">
    <div class="cover-photo" role="img" aria-label="Photo of a smiling nurse talking with an elderly woman patient in a bright room"></div>
    <div class="title-ring"></div>
    <div class="title-block">
      <h1 class="book-title">Crimson Lantern<br>Harbor</h1>
      <div class="topic">Nursing</div>
    </div>
    <div class="author">Author’s Name</div>
  </article>

  <article class="cover cover--family">
    <div class="cover-photo" role="img" aria-label="Photo of a happy family of four outdoors in warm sunlight"></div>
    <div class="title-ring"></div>
    <div class="title-block">
      <h1 class="book-title">Crimson Lantern<br>Harbor</h1>
      <div class="topic topic--long">Family and Faith</div>
    </div>
    <div class="author">Author’s Name</div>
  </article>

  <article class="cover cover--military">
    <div class="cover-photo" role="img" aria-label="Photo of a soldier in camouflage uniform standing before a pale building"></div>
    <div class="title-ring"></div>
    <div class="title-block">
      <h1 class="book-title">Crimson Lantern<br>Harbor</h1>
      <div class="topic">Military</div>
    </div>
    <div class="author">Author’s Name</div>
  </article>
</main>
</body>
</html>
```